Packaging design for a low carb bar

I am producing a low carb / high fat bar, therefore I would like to have a light weighted modern design. The background color pastel light or something like that. The package should be focused on fitness-active individuals who are looking for healthy low carb snacks. Preliminary packaging size, logo, and more details on what should be attached to the packaging are attached. Thank you!

```html
<!DOCTYPE html>
<html lang="en">
<head>
<meta charset="utf-8">
<title>Greenmere Keto Bar – Almond Coconut &amp; Chia</title>
<link rel="stylesheet" href="https://fonts.googleapis.com/css2?family=Plus+Jakarta+Sans:wght@400;500;700;800&display=swap">
<style>
  :root {
    --teal: #2a8a97;
    --teal-mid: #4aa2af;
    --teal-pale: #bfdfe4;
    --paper: #ffffff;
    --paper-tint: #f6f7f7;
    --white: #ffffff;
    --coconut: #f3f0ea;
    --husk: #7a4f30;
    --almond: #b87548;
  }
  * { margin: 0; padding: 0; box-sizing: border-box; }
  html, body { width: 1200px; height: 277px; overflow: hidden; background: var(--paper); }
  .wrapper-label {
    position: relative;
    width: 1200px;
    height: 277px;
    overflow: hidden;
    font-family: "Plus Jakarta Sans", sans-serif;
    color: var(--teal);
  }
  .nut-pattern {
    position: absolute;
    inset: 0;
    background: linear-gradient(90deg, var(--paper-tint), var(--paper) 50%, var(--paper-tint));
  }
  .brand {
    position: absolute;
    left: 58px;
    top: 29px;
    width: 224px;
    height: 224px;
    border-radius: 50%;
    background: var(--teal-pale);
    display: flex;
    align-items: center;
    justify-content: center;
  }
  .brand-name {
    font-size: 28px;
    font-weight: 400;
    letter-spacing: 2px;
    text-transform: uppercase;
    color: var(--teal);
  }
  .product-title {
    position: absolute;
    left: 355px;
    top: 52px;
    font-weight: 700;
    font-size: 92px;
    line-height: 79px;
    letter-spacing: -3px;
  }
  .product-title span { display: block; }
  .diet-badge {
    position: absolute;
    left: 501px;
    top: 161px;
    width: 70px;
    height: 46px;
    border-radius: 6px;
    background: var(--teal);
    color: var(--white);
    font-weight: 700;
    font-size: 16px;
    line-height: 17px;
    display: flex;
    flex-direction: column;
    align-items: center;
    justify-content: center;
  }
  .flavour-frame {
    position: absolute;
    left: 760px;
    top: 25px;
    width: 403px;
    height: 223px;
  }
  .flavour-disc {
    position: absolute;
    left: 642px;
    top: 50px;
    width: 178px;
    height: 178px;
    border-radius: 50%;
    background: var(--teal-mid);
  }
  .flavour-photo {
    position: absolute;
    left: 18px;
    top: 42px;
    width: 142px;
    height: 94px;
    border-radius: 47px;
    background: linear-gradient(90deg, var(--husk) 0%, var(--coconut) 18%, var(--coconut) 45%, var(--husk) 58%, var(--almond) 75%, var(--husk) 100%);
  }
  .flavour-name {
    position: absolute;
    left: 874px;
    top: 51px;
    font-weight: 700;
    font-size: 56px;
    line-height: 47px;
    letter-spacing: -1.5px;
  }
  .flavour-name span { display: block; }
  .net-carbs {
    position: absolute;
    left: 881px;
    top: 213px;
    width: 196px;
    height: 35px;
    border-radius: 12px 12px 0 0;
    background: var(--teal);
    color: var(--white);
    font-size: 17px;
    font-weight: 400;
    display: flex;
    align-items: center;
    justify-content: center;
    gap: 5px;
  }
  .net-carbs strong { font-weight: 800; }
</style>
</head>
<body>
  <div class="wrapper-label">
    <div class="nut-pattern" role="img" aria-label="Faint line drawings of assorted nuts scattered across a white background"></div>

    <div class="brand">
      <span class="brand-name">Greenmere</span>
    </div>

    <h1 class="product-title"><span>Keto</span><span>Bar</span></h1>
    <div class="diet-badge"><span>LCHF</span><span>DIET</span></div>

    <svg class="flavour-frame" viewBox="0 0 403 223" aria-hidden="true">
      <path d="M12 1 H391 A11 11 0 0 0 402 12 V211 A11 11 0 0 0 391 222 H12 A11 11 0 0 0 1 211 V12 A11 11 0 0 0 12 1 Z"
            fill="none" stroke="var(--teal)" stroke-width="1.6"/>
    </svg>

    <div class="flavour-disc">
      <div class="flavour-photo" role="img" aria-label="Photo of a halved coconut and a whole almond"></div>
    </div>

    <h2 class="flavour-name"><span>Almond</span><span>Coconut</span><span>&amp; Chia</span></h2>

    <div class="net-carbs"><strong>3.5g</strong> net carbs</div>
  </div>
</body>
</html>
```